Need a cover for my Lernova course

I'm publishing a Lernova course and I need an image for the cover. The course is on Trellis.JS, which is a library for developing web applications. Trellis.JS has a standard logo that you can find here:

http://www.pixelgrove.example/wp-content/uploads/2013/05/trellis.png

Lernova has a set of guidelines for designing cover images:

https://help.lernova.example/customer/portal/articles/4820371-course-image-standards?b_id=7142

Look at the designs on their guideline. They are bold, beautiful, clean and vibrant. I want a cover design like that but with Trellis.JS logo.

Industry/Entity Type

Library

Requirements
Must have
• White clean background
Nice to have
• Play with the background to make it look more modern and appealing. It should still convey the Trellis logo but you may slightly change the ones or make the sharp corners a bit round. Or may be put a glowing effect under the logo on the white background to make it stand out.

```html
<!DOCTYPE html>
<html lang="en">
<head>
<meta charset="utf-8">
<title>Cover For Lernova – Trellis.JS Course</title>
<link rel="stylesheet" href="https://fonts.googleapis.com/css2?family=Arimo:wght@400;700&family=Comic+Neue:wght@400;700&display=swap">
<style>
  :root {
    --band-blue: #2f86e8;
    --white: #ffffff;
    --ink: #111111;
    --frame-grey: #d3d3d3;
    --frame-dark: #8a8a8a;
    --alert-red: #e0242a;
    --logo-blue: #2a7fe0;
    --glow-lime: rgba(222, 236, 60, 0.55);
    --glow-fade: rgba(222, 236, 60, 0);
    --mustard-light: #e2da36;
    --mustard-dark: #c6bc22;
    --green-light: #58b52c;
    --green-dark: #3a941c;
    --arrow-blue: #1a34d6;
    --shot-top: #f1f3f5;
    --shot-mid: #cfd8e2;
    --shot-edge: #9aa3ad;
  }
  * { box-sizing: border-box; margin: 0; padding: 0; }
  html, body { width: 1200px; height: 2432px; overflow: hidden; }
  body {
    position: relative;
    background: var(--white);
    font-family: "Arimo", Arial, sans-serif;
    color: var(--ink);
  }

  .band {
    position: absolute; left: 0; width: 1200px;
    background: var(--band-blue); color: var(--white); text-align: center;
  }
  .band--title { top: 0; height: 105px; }
  .band--simulation { top: 572px; height: 776px; }
  .band__heading { font-weight: 700; font-size: 54px; line-height: 1; padding-top: 24px; }
  .band__subheading { font-weight: 700; font-size: 30px; margin-top: 22px; }

  /* browser mock */
  .browser {
    position: absolute;
    background: var(--frame-grey);
    padding-top: var(--bar);
    overflow: hidden;
  }
  .browser__tab, .browser__address, .browser__button, .browser__dot { position: absolute; }
  .browser__tab {
    left: 4%; top: calc(var(--bar) * .3); width: 7%; height: calc(var(--bar) * .4);
    background: var(--frame-dark);
  }
  .browser__address {
    left: 13%; top: calc(var(--bar) * .28); width: 63%; height: calc(var(--bar) * .44);
    background: var(--white); border-radius: 3px;
  }
  .browser__button {
    left: 79%; top: calc(var(--bar) * .28); width: 13%; height: calc(var(--bar) * .44);
    background: var(--white); border-radius: 3px;
  }
  .browser__dot {
    right: 2.4%; top: calc(var(--bar) * .22); width: calc(var(--bar) * .5); height: calc(var(--bar) * .5);
    background: var(--alert-red); border-radius: 50%;
  }
  .browser__screen {
    width: 100%; height: 100%;
    display: flex; align-items: center; justify-content: center;
  }
  .screen--white-glow {
    background:
      radial-gradient(ellipse 45% 55% at 50% 55%, var(--glow-lime) 0%, var(--glow-fade) 100%),
      var(--white);
  }
  .screen--mustard { background: linear-gradient(160deg, var(--mustard-light), var(--mustard-dark)); }
  .screen--green { background: linear-gradient(160deg, var(--green-light), var(--green-dark)); }
  .course-name { font-weight: 700; color: var(--logo-blue); line-height: 1; }

  .browser--cover { left: 154px; top: 158px; width: 515px; height: 284px; --bar: 28px; }
  .browser--cover .course-name { font-size: 64px; }
  .browser--reference { left: 336px; top: 1520px; width: 546px; height: 294px; --bar: 32px; }
  .browser--reference .course-name { font-size: 70px; }
  .browser--alt-a { left: 77px; top: 2143px; width: 505px; height: 320px; --bar: 32px; }
  .browser--alt-b { left: 618px; top: 2143px; width: 515px; height: 320px; --bar: 32px; }
  .browser--alt-a .course-name, .browser--alt-b .course-name { font-size: 70px; }

  /* dimensions */
  .dimension { position: absolute; left: 0; top: 0; }
  .dimension-label { position: absolute; font-size: 30px; }
  .dimension-label--height { left: 30px; top: 280px; }
  .dimension-label--width { left: 360px; top: 476px; }

  /* safe area */
  .safe-area { position: absolute; left: 776px; top: 158px; width: 336px; height: 288px; }
  .safe-area__crop {
    position: absolute; left: 36px; top: 28px; width: 264px; height: 230px;
    display: flex; align-items: center; justify-content: center;
    border: 2px solid var(--frame-grey);
  }
  .safe-area__crop .course-name { font-size: 58px; }
  .safe-area__label {
    position: absolute; left: 770px; top: 468px; width: 348px;
    text-align: center; font-weight: 700; font-size: 32px;
  }

  /* browser listing */
  .listing-screenshot {
    position: absolute; left: 142px; top: 752px; width: 912px; height: 525px;
    background: linear-gradient(180deg, var(--shot-top) 0%, var(--shot-mid) 100%);
    border: 6px solid var(--shot-edge);
  }

  /* annotations */
  .note {
    position: absolute; font-family: "Comic Neue", "Comic Sans MS", cursive;
    font-size: 31px; line-height: 39px; color: var(--ink); white-space: nowrap;
  }
  .note--reference { left: 370px; top: 1426px; }
  .note--contrast { left: 97px; top: 1880px; }
  .note--shadow { left: 728px; top: 1862px; }
  .annotations { position: absolute; left: 0; top: 0; }

  .section-heading {
    position: absolute; left: 0; width: 1200px; top: 2044px;
    text-align: center; font-weight: 700; font-size: 48px;
  }
</style>
</head>
<body>
  <header class="band band--title">
    <h1 class="band__heading">Cover For Lernova</h1>
  </header>

  <section class="cover-spec">
    <svg class="dimension" width="1200" height="520" viewBox="0 0 1200 520" aria-hidden="true">
      <g stroke="#111" stroke-width="3" fill="none">
        <line x1="86" y1="158" x2="86" y2="262"/>
        <line x1="86" y1="336" x2="86" y2="442"/>
        <line x1="72" y1="158" x2="100" y2="158"/>
        <line x1="72" y1="442" x2="100" y2="442"/>
        <line x1="154" y1="493" x2="345" y2="493"/>
        <line x1="490" y1="493" x2="669" y2="493"/>
        <line x1="154" y1="479" x2="154" y2="507"/>
        <line x1="669" y1="479" x2="669" y2="507"/>
        <polyline points="776,198 776,158 830,158"/>
        <polyline points="1058,158 1112,158 1112,198"/>
        <polyline points="776,406 776,446 830,446"/>
        <polyline points="1058,446 1112,446 1112,406"/>
      </g>
    </svg>
    <span class="dimension-label dimension-label--height">1152 px</span>
    <span class="dimension-label dimension-label--width">2048 px</span>

    <div class="browser browser--cover">
      <span class="browser__tab"></span><span class="browser__address"></span>
      <span class="browser__button"></span><span class="browser__dot"></span>
      <div class="browser__screen screen--white-glow"><span class="course-name">Trellis</span></div>
    </div>

    <div class="safe-area">
      <div class="safe-area__crop screen--white-glow"><span class="course-name">Trellis</span></div>
    </div>
    <p class="safe-area__label">Safe Area</p>
  </section>

  <section class="band band--simulation">
    <h2 class="band__heading">Browser Simulation</h2>
    <p class="band__subheading">The yellow background draws more attention causing a greater emphasis</p>
  </section>
  <div class="listing-screenshot" role="img" aria-label="Screenshot of the Lernova course listing page in a browser, with the Trellis cover among other course thumbnails"></div>

  <section class="reference">
    <p class="note note--reference">visual reference for internet</p>
    <div class="browser browser--reference">
      <span class="browser__tab"></span><span class="browser__address"></span>
      <span class="browser__button"></span><span class="browser__dot"></span>
      <div class="browser__screen screen--white-glow"><span class="course-name">Trellis</span></div>
    </div>
    <svg class="annotations" width="1200" height="2000" viewBox="0 0 1200 2000" aria-hidden="true">
      <g stroke="var(--arrow-blue)" stroke-width="3" fill="none" stroke-linecap="round" stroke-linejoin="round">
        <path d="M554 1472 Q562 1496 556 1530"/>
        <path d="M546 1518 L556 1532 L566 1518"/>
        <path d="M385 1784 Q372 1830 340 1860"/>
        <path d="M338 1844 L338 1862 L354 1858"/>
        <path d="M811 1800 Q860 1796 890 1846"/>
        <path d="M874 1838 L890 1848 L892 1830"/>
      </g>
    </svg>
    <p class="note note--contrast">Yellow and blue have more contrast</p>
    <p class="note note--shadow">Shadow to highlight more of<br>the background and make it<br>more modern</p>
  </section>

  <section class="alternatives">
    <h2 class="section-heading">Some Other Good Colors</h2>
    <div class="browser browser--alt-a">
      <span class="browser__tab"></span><span class="browser__address"></span>
      <span class="browser__button"></span><span class="browser__dot"></span>
      <div class="browser__screen screen--mustard"><span class="course-name">Trellis</span></div>
    </div>
    <div class="browser browser--alt-b">
      <span class="browser__tab"></span><span class="browser__address"></span>
      <span class="browser__button"></span><span class="browser__dot"></span>
      <div class="browser__screen screen--green"><span class="course-name">Trellis</span></div>
    </div>
  </section>
</body>
</html>
```